Dorrish Electric Ltd

Looking for a single page website and Facebook page design. I am an electrical contractor based on Vancouver Island. I do service, custom homes, residential and commercial installations. My company just started out, so I don't have any pictures of installs yet. I have 25 years experience. I would like the colors to be my logo colors black and I have a black Corvan Ridgeback that will be my vehicle which I will have a wrap for.
Updates

I just posted the contest today, not sure why the deadline is the same day.

Went on vacation/holiday

Industry/Entity Type

Electrician

Requirements
Must have
• Services provided, About me section, quote section,
Nice to have
• I am not quite sure yet, I need to see some designs first .

```html
<!DOCTYPE html>
<html lang="en">
<head>
<meta charset="utf-8">
<title>Dorrish Electric Ltd</title>
<link href="https://fonts.googleapis.com/css2?family=Montserrat:wght@600;700;800&family=Lato:ital,wght@0,400;0,700;1,400&display=swap" rel="stylesheet">
<style>
:root{
  --yellow:#fdd835;
  --yellow-deep:#f5c518;
  --black:#111111;
  --dark:#1c1c1c;
  --ink:#222222;
  --muted:#8a8a8a;
  --line:#e5e5e5;
  --white:#ffffff;
  --pale:#f3f3f3;
}
*{box-sizing:border-box;margin:0;padding:0}
html,body{width:1200px;height:3066px;overflow:hidden}
body{position:relative;background:var(--white);font-family:'Lato',sans-serif;color:var(--ink);font-size:10px}
.abs{position:absolute}
h2,h3,h4,.mont{font-family:'Montserrat',sans-serif}
.wrap{position:absolute;left:244px;width:712px}

/* top bar */
.topbar{left:0;top:0;width:1200px;height:24px;background:var(--dark)}
.topbar .tag{left:244px;top:7px;color:var(--yellow);font-size:9px}
.topbar .links{right:244px;top:0;display:flex;height:24px}
.topbar .links span{color:#999;font-size:9px;padding:7px 24px;border-left:1px solid #333}
.topbar .links span:last-child{border-right:1px solid #333}

/* header */
.header{left:0;top:24px;width:1200px;height:82px;background:var(--black)}
.brand{left:250px;top:20px;width:100px;text-align:center}
.brand .dot{width:40px;height:40px;border-radius:50%;border:2px solid var(--white);margin:0 auto 4px}
.brand .name{color:var(--white);font-family:'Montserrat',sans-serif;font-weight:700;font-size:8px}
.contact{top:26px;display:flex;gap:10px;align-items:flex-start}
.contact b{display:block;color:var(--white);font-family:'Montserrat',sans-serif;font-size:11px}
.contact small{color:var(--yellow);font-size:9px}
.contact small.grey{color:#aaa}
.social-strip{left:868px;top:86px;width:332px;height:35px;background:var(--yellow);clip-path:polygon(0 50%,14px 0,100% 0,100% 100%,14px 100%)}
.social-strip .ic{position:absolute;top:11px;width:12px;height:12px;background:var(--black);border-radius:2px}

/* nav */
.nav{left:0;top:106px;width:1200px;height:44px;background:var(--white);border-bottom:1px solid var(--line)}
.nav ul{position:absolute;left:256px;top:16px;display:flex;gap:25px;list-style:none}
.nav li{font-family:'Montserrat',sans-serif;font-weight:600;font-size:9px;color:#333;position:relative}
.nav .new{position:absolute;left:70px;top:-9px;background:#d32f2f;color:#fff;font-size:6px;padding:1px 3px}

/* hero */
.hero{left:0;top:150px;width:1200px;height:410px;background:linear-gradient(90deg,#5e5a55 0%,#9c7a46 30%,#c98e33 50%,#9c7a46 72%,#4c4a48 100%)}
.hero .shade{inset:0;background:rgba(0,0,0,.25)}
.hex{width:66px;height:58px;background:var(--yellow);clip-path:polygon(25% 0,75% 0,100% 50%,75% 100%,25% 100%,0 50%)}
.hero h1{left:0;width:1200px;top:170px;text-align:center;color:var(--white);font-family:'Montserrat',sans-serif;font-weight:800;font-size:30px}
.btn{display:inline-block;background:var(--yellow);color:var(--black);font-family:'Montserrat',sans-serif;font-weight:700;font-size:8px;padding:8px 12px}
.hero .logo-box{left:524px;top:274px;width:120px;height:80px;background:var(--black);text-align:center;padding-top:14px}
.arrow-btn{width:38px;height:38px;background:var(--white);top:187px}
.dots{left:568px;top:386px;display:flex;gap:4px}
.dots i{width:18px;height:3px;background:#ccc}
.dots i.on{background:var(--white)}

/* section heads */
.sec-title{font-family:'Montserrat',sans-serif;font-weight:700;font-size:21px;color:var(--black)}
.sec-sub{font-size:9px;color:#777;margin-top:4px}

/* features */
.feature{top:660px;width:225px;height:126px;border:1px solid var(--yellow);background:var(--white)}
.feature .yl{right:0;top:0;width:70px;height:100%;background:var(--yellow);clip-path:polygon(25% 0,100% 0,100% 100%,25% 100%,0 50%)}
.feature h4{left:13px;top:20px;width:130px;font-size:11px;font-weight:700}
.feature p{left:13px;top:42px;width:140px;font-size:9px;line-height:1.55;color:#888}

/* about */
.about-left{left:0;top:849px;width:205px;height:365px;background:linear-gradient(135deg,#eee,#dcdcdc);clip-path:polygon(0 0,100% 0,100% 0,18% 50%,100% 100%,0 100%,0 0)}
.about-photo{left:686px;top:849px;width:514px;height:365px;background:linear-gradient(120deg,#c9c9c9,#9a8a78 55%,#3d3a44);clip-path:polygon(13% 0,100% 0,100% 100%,13% 100%,0 50%)}
.about h2{left:244px;top:893px;width:360px;font-size:20px;line-height:1.25}
.about .lead{left:244px;top:974px;width:345px;font-size:9px;line-height:1.55;color:#888}
.point{width:160px;font-size:9px;line-height:1.55;color:#888;border-left:2px solid var(--yellow);padding-left:8px}

/* services */
.svc-head{left:0;top:1214px;width:1200px;height:131px;background:var(--dark)}
.svc-head h2{color:var(--white)}
.svc{width:225px;height:145px;background:var(--white)}
.svc .ph{left:0;top:0;width:225px;height:120px}
.svc .bar{left:0;top:112px;width:225px;height:33px;background:var(--yellow)}
.svc .bar b{position:absolute;right:12px;top:11px;font-family:'Montserrat',sans-serif;font-size:10px;color:var(--black)}
.svc .hx{left:30px;top:104px;width:56px;height:48px;background:var(--black);clip-path:polygon(25% 0,75% 0,100% 50%,75% 100%,25% 100%,0 50%)}

/* works */
.works-bg{left:0;top:1714px;width:1200px;height:120px;background:linear-gradient(90deg,#fff 0%,#fff 55%,#eee 100%)}
.filters{left:244px;top:1804px;height:28px;display:flex}
.filters span{font-family:'Montserrat',sans-serif;font-weight:700;font-size:8px;padding:10px 18px;background:var(--yellow)}
.filters span.on{background:var(--white);border:1px solid var(--line)}
.shot{top:1834px;width:240px;height:181px}
.round{width:26px;height:26px;border-radius:50%;background:var(--yellow);top:1911px}

/* testimonial */
.quote-box{left:244px;top:2116px;width:712px;height:79px;border:1px solid var(--yellow)}
.quote-box .mark{left:18px;top:14px;font-family:'Montserrat',sans-serif;font-weight:800;font-size:42px;color:var(--yellow);line-height:1}
.quote-box p{left:63px;top:28px;width:620px;font-style:italic;font-size:10px;color:#777;line-height:1.8}
.avatar{left:244px;top:2217px;width:43px;height:43px;background:linear-gradient(135deg,#555,#2a3a4a)}

/* get a quote */
.q-left{left:0;top:2303px;width:560px;height:337px;background:linear-gradient(135deg,#d9dde3 0%,#aab4c2 40%,#e0a638 65%,#c9c3b8 100%)}
.q-right{left:940px;top:2303px;width:260px;height:337px;background:linear-gradient(90deg,#e9e6e0,#f5f3ef)}
.q-panel{left:550px;top:2303px;width:510px;height:337px;background:var(--black);clip-path:polygon(0 0,90% 0,100% 50%,90% 100%,0 100%)}
.field{height:30px;background:var(--white);color:#999;font-size:8px;padding:10px 10px}

/* partners */
.partner{top:2672px;width:113px;height:59px;border:1px solid #ddd}
.partner i{position:absolute;left:44px;top:18px;width:24px;height:24px;background:#bbb;border-radius:50%}

/* footer */
.footer{left:0;top:2780px;width:1200px;height:286px;background:var(--dark)}
.footer h4{color:var(--white);font-size:13px;font-weight:700}
.footer .rule{height:2px;background:var(--yellow);margin-top:10px}
.footer p,.footer li{color:#9a9a9a;font-size:8px;line-height:2.2;list-style:none}
.foot-strip{left:0;top:2990px;width:408px;height:31px;background:var(--yellow);clip-path:polygon(0 0,97% 0,100% 50%,97% 100%,0 100%)}
.foot-strip .ic{position:absolute;top:10px;width:11px;height:11px;background:var(--black);border-radius:2px}
.totop{left:1156px;top:3016px;width:26px;height:26px;background:var(--yellow-deep)}
</style>
</head>
<body>

<!-- top bar -->
<div class="abs topbar">
  <span class="abs tag">Your Trusted 24 Hours Electrical Service Provider!</span>
  <div class="abs links"><span>Information</span><span>Extras</span><span>Alternative Pages</span></div>
</div>

<!-- header -->
<div class="abs header">
  <svg class="abs" style="left:340px;top:0" width="42" height="82" viewBox="0 0 42 82"><polyline points="4,0 36,41 4,82" fill="none" stroke="#fdd835" stroke-width="6"/></svg>
  <div class="abs brand"><div class="dot"></div><div class="name">Dorrish Electric Ltd</div></div>
  <div class="abs contact" style="left:420px">
    <svg width="22" height="22" viewBox="0 0 24 24"><path d="M6.6 10.8a15 15 0 006.6 6.6l2.2-2.2a1 1 0 011-.25 11 11 0 003.6.6 1 1 0 011 1V20a1 1 0 01-1 1A17 17 0 013 4a1 1 0 011-1h3.5a1 1 0 011 1 11 11 0 00.6 3.6 1 1 0 01-.25 1z" fill="#fdd835"/></svg>
    <div><b>1-250-48-316</b><small>hello@dorrishelectric.ca</small></div>
  </div>
  <div class="abs contact" style="left:578px">
    <svg width="24" height="22" viewBox="0 0 24 22"><path d="M12 1L1 11h3v10h6v-6h4v6h6V11h3z" fill="#fdd835"/></svg>
    <div><b>27 Harbour View Road</b><small class="grey">Nanaimo, BC.</small></div>
  </div>
  <svg class="abs" style="left:913px;top:35px" width="11" height="11" viewBox="0 0 12 12"><circle cx="5" cy="5" r="3.5" fill="none" stroke="#fdd835" stroke-width="2"/><line x1="8" y1="8" x2="11" y2="11" stroke="#fdd835" stroke-width="2"/></svg>
  <svg class="abs" style="left:935px;top:33px" width="13" height="13" viewBox="0 0 14 14"><path d="M1 2h2l2 7h7l1.5-5H4" fill="none" stroke="#fdd835" stroke-width="2"/><circle cx="6" cy="12" r="1.3" fill="#fdd835"/><circle cx="11" cy="12" r="1.3" fill="#fdd835"/></svg>
  <span class="abs" style="left:943px;top:26px;width:10px;height:10px;border-radius:50%;background:#444;color:#fff;font-size:6px;text-align:center;line-height:10px">0</span>
</div>
<div class="abs social-strip">
  <i class="ic" style="left:8px;top:12px;width:0;height:0;background:none"></i>
  <i class="ic" style="left:30px"></i><i class="ic" style="left:70px"></i><i class="ic" style="left:110px"></i><i class="ic" style="left:150px"></i>
</div>

<!-- nav -->
<div class="abs nav">
  <ul>
    <li>HOME</li><li>COST CALCULATOR<span class="new">NEW</span></li><li>PROJECTS</li><li>OUR SERVICES</li><li>PAGES</li><li>BLOG</li><li>SHOP</li><li>CONTACT</li>
  </ul>
</div>

<!-- hero -->
<div class="abs hero" role="img" aria-label="Tradesmen in hard hats painting an orange wall">
  <div class="abs shade"></div>
  <div class="abs hex" style="left:555px;top:92px"></div>
  <svg class="abs" style="left:572px;top:106px" width="32" height="30" viewBox="0 0 32 30"><path d="M4 14L16 4l12 10M7 12v14h18V12M12 26v-7h8v7" fill="none" stroke="#111" stroke-width="2"/></svg>
  <h1 class="abs">WE CAN DO ANYTHING!</h1>
  <span class="abs btn" style="left:522px;top:236px;width:120px;text-align:center">FIND OUT MORE »</span>
  <div class="abs logo-box">
    <div style="width:38px;height:38px;border-radius:50%;border:2px solid #fff;margin:0 auto 6px"></div>
    <div class="mont" style="color:#fff;font-weight:700;font-size:7px">Dorrish Electric Ltd</div>
  </div>
  <div class="abs arrow-btn" style="left:25px"><svg width="38" height="38"><polyline points="21,15 17,19 21,23" fill="none" stroke="#333" stroke-width="1.2"/></svg></div>
  <div class="abs arrow-btn" style="left:1139px"><svg width="38" height="38"><polyline points="17,15 21,19 17,23" fill="none" stroke="#333" stroke-width="1.2"/></svg></div>
  <div class="abs dots"><i></i><i class="on"></i><i></i></div>
</div>

<!-- features -->
<div class="wrap" style="top:604px">
  <h2 class="sec-title">Our Features</h2>
  <p class="sec-sub">From complete turn key to project manager. Leave the building to the professionals.</p>
</div>
<div class="abs feature" style="left:244px">
  <div class="abs yl"></div>
  <svg class="abs" style="right:14px;top:50px" width="26" height="26" viewBox="0 0 26 26"><path d="M3 23L15 11M11 3l12 12M3 3l8 8M23 23l-6-6" stroke="#111" stroke-width="1.6" fill="none"/></svg>
  <h4 class="abs mont">Professional HandyMan</h4>
  <p class="abs" style="top:48px">From exhaust fan assessment to reviewing attic space and cleaning refrigerator coils to give you a safe life.</p>
</div>
<div class="abs feature" style="left:487px;height:113px">
  <div class="abs yl"></div>
  <svg class="abs" style="right:18px;top:44px" width="24" height="24" viewBox="0 0 24 24"><circle cx="12" cy="12" r="10" fill="none" stroke="#111" stroke-width="1.4"/><path d="M12 6v6h-4" stroke="#111" stroke-width="1.4" fill="none"/></svg>
  <h4 class="abs mont">24/7 Services</h4>
  <p class="abs" style="top:36px">If you are in emergency situation, please do not worry. We provide 24/7 service. Whenever you call, we service you.</p>
</div>
<div class="abs feature" style="left:731px;height:113px">
  <div class="abs yl"></div>
  <svg class="abs" style="right:12px;top:46px" width="28" height="20" viewBox="0 0 28 20"><rect x="4" y="2" width="22" height="14" fill="none" stroke="#111" stroke-width="1.4"/><rect x="1" y="5" width="22" height="14" fill="none" stroke="#111" stroke-width="1.4"/><circle cx="12" cy="12" r="3" fill="none" stroke="#111" stroke-width="1.4"/></svg>
  <h4 class="abs mont">Affordable Price</h4>
  <p class="abs" style="top:36px">We do more than a renovation service- we check for glitches that need attention to keep you safe and save your money.</p>
</div>

<!-- about -->
<div class="abs about-left" role="img" aria-label="Faded workshop backdrop"></div>
<div class="abs about-photo" role="img" aria-label="Electrician in a cap looking up at a ceiling fixture"></div>
<div class="abs" style="left:686px;top:960px;width:60px;height:120px;background:#c62828;clip-path:polygon(100% 0,100% 100%,20% 60%)"></div>
<div class="about">
  <h2 class="abs sec-title">We Are Professional &amp; Thoughtful HandyMan</h2>
  <p class="abs lead">Handyman was established in response to the growing need for quality housing and commercial space in the city. Since then, we have grown to be one of the leading real estate developers serving the needs of a discerning clientele.</p>
  <p class="abs point" style="left:244px;top:1033px">We have high quality labor who are trained every year with latest technology.</p>
  <p class="abs point" style="left:418px;top:1033px">We have 15 year experience in building market.</p>
  <p class="abs point" style="left:244px;top:1088px">Material from the top partner in market.</p>
  <p class="abs point" style="left:418px;top:1088px">Update the tendency from around the world.</p>
  <span class="abs btn" style="left:244px;top:1146px">VIEW OUR PROJECTS &nbsp;»</span>
</div>

<!-- services -->
<div class="abs svc-head">
  <div class="wrap" style="top:44px">
    <h2 class="sec-title" style="color:#fff">Our Services</h2>
    <p class="sec-sub" style="color:var(--yellow)">From complete turn key to project manager. Leave the building to the professionals.</p>
  </div>
</div>

<div class="abs svc" style="left:244px;top:1364px"><div class="abs ph" role="img" aria-label="Worker renovating a white room" style="background:linear-gradient(135deg,#eee,#c7c2bb)"></div><div class="abs bar"><b>Renovation</b></div><div class="abs hx"></div></div>
<div class="abs svc" style="left:487px;top:1364px"><div class="abs ph" role="img" aria-label="Electrician in a kitchen" style="background:linear-gradient(135deg,#555,#ddd)"></div><div class="abs bar"><b>Electrical</b></div><div class="abs hx"></div></div>
<div class="abs svc" style="left:731px;top:1364px"><div class="abs ph" role="img" aria-label="Painter with a brush" style="background:linear-gradient(135deg,#d9c89a,#3f5a86)"></div><div class="abs bar"><b>Painting</b></div><div class="abs hx"></div></div>
<div class="abs svc" style="left:244px;top:1527px"><div class="abs ph" role="img" aria-label="Plumber fixing a sink" style="background:linear-gradient(135deg,#f1f1f1,#2d3346)"></div><div class="abs bar"><b>Plumbing</b></div><div class="abs hx"></div></div>
<div class="abs svc" style="left:487px;top:1527px"><div class="abs ph" role="img" aria-label="Drilling a heating panel" style="background:linear-gradient(135deg,#e7e7e7,#b8654e)"></div><div class="abs bar"><b>Heating</b></div><div class="abs hx"></div></div>
<div class="abs svc" style="left:731px;top:1527px"><div class="abs ph" role="img" aria-label="Roofer laying red tiles" style="background:linear-gradient(135deg,#c7563e,#e2b84a)"></div><div class="abs bar"><b>Roofing</b></div><div class="abs hx"></div></div>

<!-- works -->
<div class="abs works-bg"></div>
<div class="wrap" style="top:1754px">
  <h2 class="sec-title">Our Works</h2>
  <p class="sec-sub">We let our quality work and commitment to customer satisfaction be our slogan.</p>
</div>
<div class="abs filters"><span class="on">ALL WORKS</span><span>ELECTRICAL</span><span>INTERIOR</span><span>PAINTING</span><span>PLUMBING</span><span style="clip-path:polygon(0 0,88% 0,100% 50%,88% 100%,0 100%);padding-right:26px">REPAIR</span></div>
<div class="abs shot" style="left:0" role="img" aria-label="Plumber at a bathroom sink" style=""><div style="width:100%;height:100%;background:linear-gradient(135deg,#f2f2f2,#2b3044)"></div></div>
<div class="abs shot" style="left:240px" role="img" aria-label="Two workers by a house with a ladder"><div style="width:100%;height:100%;background:linear-gradient(135deg,#f4f2ea,#9fb3c6)"></div></div>
<div class="abs shot" style="left:480px" role="img" aria-label="Empty wooden interior"><div style="width:100%;height:100%;background:linear-gradient(135deg,#e6b46c,#9b6a35)"></div></div>
<div class="abs shot" style="left:720px" role="img" aria-label="Worker in a kitchen"><div style="width:100%;height:100%;background:linear-gradient(135deg,#444,#e0e0e0)"></div></div>
<div class="abs shot" style="left:960px" role="img" aria-label="Unfinished kitchen cabinets"><div style="width:100%;height:100%;background:linear-gradient(135deg,#f0e6d3,#d7bf92)"></div></div>
<div class="abs round" style="left:4px"><svg width="26" height="26"><polyline points="15,9 11,13 15,17" fill="none" stroke="#111" stroke-width="2"/></svg></div>
<div class="abs round" style="left:1168px"><svg width="26" height="26"><polyline points="11,9 15,13 11,17" fill="none" stroke="#111" stroke-width="2"/></svg></div>

<!-- testimonials -->
<div class="wrap" style="top:2054px">
  <h2 class="sec-title">Testimonials</h2>
  <p class="sec-sub">Creating a sustainable future through building preservation, green architecture, and smart design.</p>
</div>
<div class="abs quote-box">
  <span class="abs mark">“</span>
  <p class="abs">I have used the services of your company on a few occasions. Your crews are always personable, prompt and efficient. The work performed has been very good and as described. I have confidence in recommending their services to anyone.</p>
</div>
<div class="abs avatar" role="img" aria-label="Client portrait"></div>
<div class="abs" style="left:300px;top:2218px">
  <b class="mont" style="font-size:11px;font-weight:600">Marla Keswick</b>
  <p style="color:#999;font-size:9px;margin-top:3px">Owner of Keswick Homes</p>
  <p style="font-style:italic;font-size:9px;margin-top:3px">http://keswickhomes.ca</p>
</div>
<div class="abs" style="left:890px;top:2226px;display:flex;gap:5px"><i style="width:18px;height:3px;background:var(--yellow)"></i><i style="width:18px;height:3px;background:#ddd"></i><i style="width:18px;height:3px;background:#ddd"></i></div>

<!-- quote -->
<div class="abs q-left" role="img" aria-label="Worker in a tool belt holding a yellow cordless drill"></div>
<div class="abs q-right" role="img" aria-label="Bright kitchen interior"></div>
<div class="abs q-panel"></div>
<div class="abs" style="left:609px;top:2348px;width:347px">
  <h2 class="sec-title" style="color:#fff">Get A Quick Quote</h2>
  <p class="sec-sub" style="color:var(--yellow);line-height:1.5">Send us an email by entering your details and any comments you may have in the form.</p>
</div>
<div class="abs field" style="left:609px;top:2422px;width:171px">Your Name</div>
<div class="abs field" style="left:786px;top:2422px;width:170px">Your Email</div>
<div class="abs field" style="left:609px;top:2460px;width:171px">Subject</div>
<div class="abs field" style="left:786px;top:2460px;width:170px">Phone</div>
<div class="abs field" style="left:609px;top:2498px;width:347px;height:68px">Your message</div>
<span class="abs btn" style="left:609px;top:2575px">SEND MESSAGE</span>

<!-- partners -->
<div class="abs partner" style="left:244px"><i></i></div>
<div class="abs partner" style="left:364px"><i></i></div>
<div class="abs partner" style="left:484px"><i></i></div>
<div class="abs partner" style="left:604px"><i></i></div>
<div class="abs partner" style="left:724px"><i></i></div>
<div class="abs partner" style="left:844px"><i></i></div>
<div class="abs" style="left:244px;top:2742px;display:flex;gap:4px"><i style="width:18px;height:3px;background:var(--yellow)"></i><i style="width:18px;height:3px;background:#ddd"></i></div>

<!-- footer -->
<div class="abs footer">
  <div class="abs" style="left:244px;top:38px;width:225px">
    <h4 class="mont" style="font-size:15px;font-weight:600"><span style="display:inline-block;width:12px;height:12px;background:var(--yellow);margin-right:6px"></span>Renovation</h4>
    <p style="margin-top:16px;line-height:2.2">Our mission is to provide the best renovation service at an reasonable price without sacrificing quality. You will be satisfy with our work knowing we take the necessary steps to meet your needs and get the job done right</p>
  </div>
  <div class="abs" style="left:487px;top:43px;width:225px">
    <h4 class="mont">Information</h4><div class="rule"></div>
    <ul style="display:grid;grid-template-columns:1fr 1fr;margin-top:12px">
      <li>› Blog</li><li>› Projects</li><li>› Services</li><li>› Information</li><li>› Extras</li><li>› About us</li><li>› Contact</li><li>› Shop</li>
    </ul>
  </div>
  <div class="abs" style="left:731px;top:43px;width:225px">
    <h4 class="mont">Renovation Office</h4><div class="rule"></div>
    <ul style="margin-top:12px">
      <li>⌖ &nbsp;&nbsp;27 Harbour View Road, Nanaimo, BC.</li>
      <li>✆ &nbsp;&nbsp;(250) 555 0142</li>
      <li>✉ &nbsp;&nbsp;hello@dorrishelectric.ca</li>
      <li>☏ &nbsp;&nbsp;(250) 555 0187</li>
      <li>◷ &nbsp;&nbsp;Mon - Sat: 9:00 - 18:00</li>
    </ul>
  </div>
</div>
<div class="abs foot-strip"><i class="ic" style="left:260px"></i><i class="ic" style="left:298px"></i><i class="ic" style="left:338px"></i><i class="ic" style="left:378px"></i></div>
<div class="abs totop"><svg width="26" height="26"><polyline points="8,16 13,10 18,16" fill="none" stroke="#fff" stroke-width="2"/></svg></div>

</body>
</html>
```